Blue Harbor Car Finance Home Page

We need a desktop version mock up (we will base our mobile version off of this) of a website homepage for our auto loan business, Blue Harbor Car Finance. This does not need to be a functioning site, just a home page mock up. We are based in the metro St. Louis, MO area. We offer "guaranteed" auto loans for all credit types. We specialize in financing for bad/no credit customers. We are able to help rebuild these type of customers' credit, all while putting them in a great late model vehicle they'll love. Our online credit app takes less than 60 seconds, doesn't require a SS# and gives a free credit score if they fill it out within 3 minutes. We are looking for an outside perspective to help us in this design process. We are not completely sure what we want, but we do want it to be professional and secure looking, all while being unique and aesthetically pleasing. We want the customer to be able to put in their zip code to be directed to the right location that can get them pre approved. I attached a wireframe with some stuff we'd like to include, but in no way does it have to be in the same layout or the same ideas. We want everyone to "go crazy" with their creative side on this. Our current site is awful, here is a link to get a better idea: www.blueharborcarfinance-example.com. Attached is our logo too, base colors off of it. Watch our video that is also attached for a better idea.

Target Market(s)

Residents of the St. Louis Missouri Metro Area that need an auto loan. 24-55 Male and Female - Lots of "urban market" customers.

Industry/Entity Type

Loan

Number of Pages Required

1 page

Colors
9bcb3b

Requirements
Must have
• An area where the customer can enter their zip code - Be creative!
Nice to have
• See wireframe attachment for ideas - Be creative!

```html
<!DOCTYPE html>
<html lang="en">
<head>
<meta charset="utf-8">
<title>Blue Harbor Car Finance – Home</title>
<link href="https://fonts.googleapis.com/css2?family=Raleway:wght@400;500;600;700;800&display=swap" rel="stylesheet">
<style>
:root{
  --mint:#f2faf5;
  --white:#ffffff;
  --ink:#1d1d1d;
  --muted:#3a3a3a;
  --panel:#444444;
  --red:#d0021b;
  --step-red:#d0000d;
  --step-blue:#22aae2;
  --step-yellow:#f8f400;
  --cta-yellow:#f2e410;
  --photo:#c9c4b8;
}
*{margin:0;padding:0;box-sizing:border-box}
html,body{width:816px;height:1200px;overflow:hidden;background:var(--white)}
body{position:relative;font-family:'Raleway',sans-serif;color:var(--ink)}
.abs{position:absolute}
.site-header{left:0;top:0;width:816px;height:88px;background:var(--mint);border-bottom:1px solid #e6efe9}
.brand{left:36px;top:26px;display:flex;align-items:center;gap:8px;font-weight:800;font-size:16px;color:#2e7d1e}
.brand-mark{width:18px;height:18px;background:#9bcb3b}
.nav a{position:absolute;top:49px;height:22px;line-height:22px;font-size:12px;color:var(--ink);text-decoration:none}
.nav .active{background:var(--cta-yellow);padding:0 8px;border-radius:3px}
.phone{left:690px;top:17px;font-size:10px;display:flex;align-items:center;gap:10px}
.search{left:674px;top:52px;width:106px;height:14px;border-bottom:1px solid #333}
.search svg{position:absolute;right:0;top:-2px}
.hero{left:32px;top:106px;width:752px;height:251px;background:var(--panel)}
.hero-photo{position:absolute;left:15px;top:16px;width:387px;height:219px;border:2px solid #fff;background:linear-gradient(135deg,#e8e6e0,var(--photo) 55%,#8f8a7e)}
.form-title{position:absolute;left:471px;top:28px;font-size:14px;color:#fff;font-weight:500}
.field-label{position:absolute;left:473px;font-size:10px;color:#fff;font-weight:600}
.field-input{position:absolute;left:538px;width:159px;height:24px;border:1px solid #fff}
.btn{position:absolute;width:159px;height:35px;display:flex;align-items:center;justify-content:center;font-weight:700;font-size:12px;border-radius:2px}
.btn-start{left:506px;top:190px;background:#fff;color:#333}
.offer{left:0;top:378px;width:816px;height:276px;background:var(--mint);border-bottom:1px solid #e6efe9}
.offer h1{position:absolute;top:20px;width:816px;text-align:center;color:var(--red);font-size:24px;font-weight:800}
.offer h2{position:absolute;top:54px;width:816px;text-align:center;font-size:12px;font-weight:700}
.perks{position:absolute;left:102px;top:106px;list-style:none;font-size:11.5px;line-height:19.2px;color:var(--muted)}
.perks li{display:flex;gap:6px}
.perks svg{flex:none;margin-top:5px}
.offer p{position:absolute;left:351px;top:106px;width:368px;font-size:11.5px;line-height:19.2px;text-align:justify;color:var(--muted)}
.btn-calc{left:538px;top:225px;background:var(--cta-yellow);color:#222}
.steps-title{left:90px;top:673px;font-size:17px;font-weight:500}
.step{position:absolute;top:710px;width:176px;height:221px;border-radius:2px}
.step .num{position:absolute;left:58px;top:14px;width:48px;height:48px;border-radius:50%;background:#fff;display:flex;align-items:center;justify-content:center;font-size:20px;color:#333;box-shadow:0 1px 3px rgba(0,0,0,.15)}
.step p{position:absolute;left:16px;top:84px;width:148px;font-size:11.5px;line-height:16.8px;font-weight:500}
.s1{left:80px;background:var(--step-red)}.s1 p{color:#7a0008}
.s2{left:313px;background:var(--step-blue)}.s2 p{color:#111}
.s3{left:545px;background:var(--step-yellow)}.s3 p{color:#222}
.testimonial{left:0;top:994px;width:816px;text-align:center;font-size:11.5px;line-height:19.4px;color:var(--muted)}
.testimonial h3{font-size:13px;font-weight:600;color:var(--ink);margin-bottom:1px}
.testimonial .who{font-weight:600;color:var(--ink)}
.arrow{top:1028px}
.footer-links{left:0;top:1135px;width:816px;text-align:center;font-size:10px;font-weight:700}
.footer{left:0;top:1150px;width:816px;height:50px;background:var(--mint);text-align:center;font-size:10px;line-height:16px;padding-top:1px;color:var(--muted)}
</style>
</head>
<body>
<header class="site-header abs">
  <div class="brand abs"><span class="brand-mark"></span>Blue Harbor Car Finance</div>
  <nav class="nav">
    <a style="left:262px">Locations</a>
    <a style="left:340px">Finance</a>
    <a class="active" style="left:402px">Center</a>
    <a style="left:473px">About</a>
    <a style="left:533px">FAQ</a>
  </nav>
  <div class="phone abs">
    <svg width="10" height="10" viewBox="0 0 24 24"><path fill="#222" d="M6.6 10.8a15 15 0 0 0 6.6 6.6l2.2-2.2c.3-.3.7-.4 1-.2 1.1.4 2.3.6 3.6.6.6 0 1 .4 1 1V20c0 .6-.4 1-1 1A17 17 0 0 1 3 4c0-.6.4-1 1-1h3.5c.6 0 1 .4 1 1 0 1.3.2 2.5.6 3.6.1.3 0 .7-.2 1z"/></svg>
    (800)555-0142
  </div>
  <div class="search abs">
    <svg width="11" height="11" viewBox="0 0 12 12"><circle cx="7.5" cy="4.5" r="3.2" fill="none" stroke="#222" stroke-width="1.6"/><line x1="5.2" y1="6.8" x2="1" y2="11" stroke="#222" stroke-width="1.8"/></svg>
  </div>
</header>

<section class="hero abs">
  <div class="hero-photo" role="img" aria-label="Photo of a couple at a table reviewing finances on a laptop"></div>
  <div class="form-title">Choose Your Location &amp; Get Started</div>
  <div class="field-label" style="top:65px">location :</div>
  <div class="field-input" style="top:60px"></div>
  <div class="field-label" style="top:96px">Names :</div>
  <div class="field-input" style="top:88px"></div>
  <div class="field-label" style="top:126px">Email :</div>
  <div class="field-input" style="top:116px"></div>
  <div class="field-label" style="top:156px">phone :</div>
  <div class="field-input" style="top:145px"></div>
  <div class="btn btn-start">GET STARTED</div>
</section>

<section class="offer abs">
  <h1>GUARANTEED FINANCING!</h1>
  <h2>FOR ALL CREDIT TYPES</h2>
  <ul class="perks">
    <li><svg width="10" height="9" viewBox="0 0 10 9"><path d="M1 5l3 3 5-7" fill="none" stroke="#222" stroke-width="2"/></svg><span>No Social Security<br>Number Required</span></li>
    <li><svg width="10" height="9" viewBox="0 0 10 9"><path d="M1 5l3 3 5-7" fill="none" stroke="#222" stroke-width="2"/></svg>Instant Approval</li>
    <li><svg width="10" height="9" viewBox="0 0 10 9"><path d="M1 5l3 3 5-7" fill="none" stroke="#222" stroke-width="2"/></svg>No Application Fees</li>
    <li><svg width="10" height="9" viewBox="0 0 10 9"><path d="M1 5l3 3 5-7" fill="none" stroke="#222" stroke-width="2"/></svg>All Credit Accepted</li>
  </ul>
  <p>Lorem ipsum dolor sit amet, consectetur adipisicing elit, sed do eiusmod tempor incididunt ut labore et dolore magna aliqua. Ut enim ad minim veniam, quis nostrud exercitation ullamco laboris nisi ut aliquip ex ea commodo consequat. Duis aute irure dolor in reprehenderit in voluptate velit esse cillum dolore eu fugiat nulla pariatur.</p>
  <div class="btn btn-calc">CALCULATE PAYMENT</div>
</section>

<h2 class="steps-title abs">Steps</h2>
<div class="step s1"><div class="num">1</div><p>Lorem ipsum dolor sit amet,consectetur adipisicing elit, sed do eiusmod tempor incididunt ut labore et dolore magna aliqua. Ut enim ad minim veniam,</p></div>
<div class="step s2"><div class="num">2</div><p>Lorem ipsum dolor sit amet, consectetur adipisicing elit, sed do eiusmod tempor incididunt ut labore et dolore magna aliqua. Ut enim ad minim veniam,</p></div>
<div class="step s3"><div class="num">3</div><p>Lorem ipsum dolor sit amet, consectetur adipisicing elit, sed do eiusmod tempor incididunt ut labore et dolore magna aliqua. Ut enim ad minim veniam,</p></div>

<svg class="arrow abs" style="left:158px" width="22" height="40" viewBox="0 0 22 40"><path d="M19 2L3 20l16 18" fill="none" stroke="#222" stroke-width="3"/></svg>
<svg class="arrow abs" style="left:636px" width="22" height="40" viewBox="0 0 22 40"><path d="M3 2l16 18L3 38" fill="none" stroke="#222" stroke-width="3"/></svg>
<section class="testimonial abs">
  <h3>Testimonial</h3>
  consectetur adipiscing elit. Proin<br>
  a elit vitae erat accumsan venenatis in ecitur velit. dapibus<br>
  fringilla. Nulla varius eleifend risus non scelerisque.<br>
  <span class="who">Satisfied Customer</span>
</section>

<nav class="footer-links abs">HOME &nbsp;|&nbsp; ABOUT &nbsp;|&nbsp; PRIVACY &nbsp;|&nbsp; CONTACT</nav>
<footer class="footer abs">© 2016 Blue Harbor Car Finance. All Rights Reserved.<br>Created by Northpoint Web Studio.</footer>
</body>
</html>
```